Web design needed for business broker

I need a design for a home page for a website I am coding. We are building a new site for an existing company and their existing site is www.qvtrades.com.au

For the office contact details will be

(02) 5384 9027
hello@qvtrades.com.au

Location – Australia Wide

Logos are attached. This will be for the brokerage side of things. I also want to set up one of the pages which will almost have its own landing page style setup for consulting. The Logo will be slightly different (Attached as colour logo with Black Background). The consulting will operate Under Quarry Vale Trade Partners, however we are changing to QV Trades for the Brokerage Arm.

The home page should have the following:

Small amount of Intro Text (Can use something from the current website for now)
Latest Listings
Recently Sold
“The Selling Process”
Also want something (either a pop up or major focus on front page to be about getting a free business appraisal).

```html
<!DOCTYPE html>
<html lang="en">
<head>
<meta charset="utf-8">
<title>QV Trades – Business Brokers</title>
<link href="https://fonts.googleapis.com/css2?family=Poppins:wght@400;500;600;700&display=swap" rel="stylesheet">
<style>
:root{
  --brown:#8b5a1f;
  --brown-dark:#6e4615;
  --gold:#c9a35b;
  --ink:#1d1d1d;
  --text:#4a4a4a;
  --muted:#777;
  --cream:#f7efe4;
  --dark:#1b1b1b;
  --white:#fff;
}
*{margin:0;padding:0;box-sizing:border-box}
html,body{width:1200px;height:5240px;overflow:hidden;background:var(--white)}
body{font-family:'Poppins',sans-serif;color:var(--text);position:relative}
.abs{position:absolute}
.section-title{position:absolute;left:0;width:1200px;text-align:center;font-size:34px;font-weight:600;color:var(--ink)}
.btn{position:absolute;background:var(--brown);color:var(--white);font-size:12px;font-weight:500;display:flex;align-items:center;justify-content:center}
.ph{position:absolute}

/* hero */
.hero{position:absolute;left:0;top:0;width:1200px;height:610px;background:linear-gradient(120deg,#3b3a3a 0%,#5d5a55 45%,#2a2826 100%)}
.hero-shade{position:absolute;inset:0;background:linear-gradient(90deg,rgba(20,20,20,.55),rgba(20,20,20,.2))}
.brand{position:absolute;left:140px;top:40px;display:flex;align-items:center;gap:10px;color:var(--gold);font-size:13px;font-weight:500}
.brand-dot{width:34px;height:34px;border-radius:50%;border:2px solid var(--gold)}
.nav{position:absolute;top:60px;left:410px;display:flex;gap:25px;font-size:12px;color:var(--white)}
.nav .active{color:var(--gold);border-bottom:1px solid var(--gold);padding-bottom:2px}
.nav-cta{left:918px;top:48px;width:140px;height:44px;border:1px solid var(--gold)}
.hero h1{position:absolute;left:138px;top:243px;font-size:29px;font-weight:600;color:var(--white)}
.hero p{position:absolute;left:142px;top:300px;width:560px;font-size:15px;line-height:28px;color:#eee}
.hero-cta{left:142px;top:438px;width:126px;height:46px;border:1px solid var(--gold)}
.video{position:absolute;left:1100px;top:172px;width:44px;text-align:center;color:var(--white);font-size:15px;font-weight:600;line-height:34px}
.play{width:44px;height:44px;border:2px solid var(--white);border-radius:50%;margin:8px auto;display:flex;align-items:center;justify-content:center}
.mouse{position:absolute;left:567px;top:578px;width:66px;height:66px;border-radius:50%;background:var(--white);box-shadow:0 3px 12px rgba(0,0,0,.2);display:flex;align-items:center;justify-content:center}

/* services */
.arrow{position:absolute;width:30px;height:50px}
.svc{position:absolute;top:795px;width:294px;height:440px;background:var(--white);box-shadow:0 2px 12px rgba(0,0,0,.08)}
.svc .ph{left:0;top:0;width:294px;height:214px;background:linear-gradient(135deg,#d7e3f2,#7a98c4)}
.svc-icon{position:absolute;left:34px;top:188px;width:54px;height:54px;border-radius:50%;background:var(--brown);border:3px solid var(--white)}
.svc h3{position:absolute;left:32px;top:260px;font-size:16px;font-weight:500;color:var(--ink)}
.svc p{position:absolute;left:32px;top:292px;width:236px;font-size:11.5px;line-height:21px;height:84px;overflow:hidden}
.link{position:absolute;font-size:11.5px;font-weight:600;color:var(--brown);text-decoration:underline}

/* process */
.process{position:absolute;left:0;top:1326px;width:1200px;height:582px;background:linear-gradient(180deg,var(--cream),#f3e6d5)}
.step{position:absolute;top:1524px;width:230px;text-align:center}
.step-circle{width:104px;height:104px;margin:0 auto;border-radius:50%;background:var(--brown);display:flex;align-items:center;justify-content:center}
.step h4{margin-top:20px;font-size:20px;font-weight:500;color:var(--ink)}
.step p{margin-top:8px;font-size:12px;line-height:21px}

/* featured */
.featured{position:absolute;left:0;top:1908px;width:1200px;height:590px;background:linear-gradient(180deg,#f1ece6,#e4ded7)}
.feat{position:absolute;top:2085px;width:446px;height:319px;background:linear-gradient(160deg,#6d6a66,#2f2d2b);color:var(--white)}
.feat h3{position:absolute;left:37px;top:44px;width:340px;font-size:14px;font-weight:500;line-height:27px}
.feat .price{position:absolute;left:37px;top:240px;font-size:28px;font-weight:600}
.feat .price small{font-size:20px;font-weight:500}
.feat .btn{left:275px;top:238px;width:144px;height:44px;border:1px solid var(--gold)}

/* quick links */
.ql{position:absolute;top:2669px;width:220px;height:217px;background:linear-gradient(180deg,#bdbdbd,#3a3a3a)}
.ql span{position:absolute;left:0;bottom:28px;width:100%;text-align:center;color:var(--white);font-size:14px;font-weight:500}

/* sold */
.sold{position:absolute;top:3088px;width:294px;height:342px;background:var(--white);box-shadow:0 2px 12px rgba(0,0,0,.08)}
.sold .ph{left:0;top:0;width:294px;height:215px;background:linear-gradient(180deg,#a59a8c,#3e3830)}
.sold .cfp{position:absolute;left:16px;top:172px;color:var(--white);font-size:17px;font-weight:600}
.sold .tag{position:absolute;left:224px;top:172px;width:56px;height:26px;background:var(--brown);border:1px solid var(--gold);color:var(--white);font-size:10px;display:flex;align-items:center;justify-content:center}
.sold h4{position:absolute;left:32px;top:252px;font-size:12px;font-weight:600;color:var(--ink)}
.sold .loc{position:absolute;left:32px;top:280px;font-size:12px;display:flex;align-items:center;gap:12px}

/* team */
.team{position:absolute;left:0;top:3604px;width:1200px;height:680px;background:linear-gradient(180deg,#2a2a2a,#161616)}
.member{position:absolute;top:206px;width:387px}
.member .ph{position:relative;width:387px;height:273px;border-radius:14px;background:linear-gradient(135deg,#7f9a74,#c9c3b8)}
.member h3{margin-top:27px;margin-left:8px;font-size:25px;font-weight:500;color:var(--white)}
.member p{margin-left:8px;font-size:12px;line-height:30px;color:#ddd}

/* news */
.news{position:absolute;top:4446px;width:293px}
.news .ph{position:relative;width:293px;height:180px}
.news .date{margin-top:18px;font-size:11px;display:flex;align-items:center;gap:8px}
.news h4{margin-top:14px;font-size:14px;font-weight:600;color:var(--ink);white-space:nowrap;overflow:hidden}
.news p{margin-top:8px;font-size:12px;line-height:21px;height:63px;overflow:hidden}
.news .link{position:static;display:block;margin-top:6px}

/* footer */
.footer{position:absolute;left:0;top:4882px;width:1200px;height:325px;background:var(--dark);color:#e5e5e5}
.fcol{position:absolute;top:76px;font-size:12px}
.fcol h5{font-size:15px;font-weight:600;color:var(--white);margin-bottom:16px}
.fcol li{list-style:none;line-height:24px}
.contact-row{display:flex;gap:10px;margin-bottom:14px;line-height:18px}
.social-row{display:flex;align-items:center;gap:10px;margin-bottom:10px}
.social-dot{width:26px;height:26px;border-radius:50%;border:1.5px solid #ccc}
.foot-brand{position:absolute;left:850px;top:92px;width:230px;text-align:center;color:var(--gold);font-size:14px;font-weight:500}
.foot-brand .brand-dot{width:70px;height:70px;margin:0 auto 18px}
.bottom-bar{position:absolute;left:0;top:5207px;width:1200px;height:33px;background:var(--brown);color:var(--white);font-size:12px;display:flex;align-items:center;justify-content:center}
</style>
</head>
<body>

<!-- Hero -->
<header class="hero">
  <div class="ph" role="img" aria-label="Businessman writing on documents at a desk with glasses and a tablet" style="inset:0;background:linear-gradient(120deg,#4a4846,#6b665f 50%,#2b2927)"></div>
  <div class="hero-shade"></div>
  <div class="brand"><span class="brand-dot"></span>QV Trades</div>
  <nav class="nav">
    <span class="active">Home</span><span>Buy</span><span>Sell</span><span>Services</span><span>About</span><span>Join Our Team</span><span>Contact</span>
  </nav>
  <div class="btn nav-cta">Free Appraisal</div>
  <h1>How much is your Business worth?</h1>
  <p>Lorem ipsum dolor sit amet, consectetur adipiscing elit, sed do eiusmod tempor incididunt ut labore et dolore magna aliqua. Quis ipsum suspendisse ultrices gravida. Risus commodo viverra maecenas accumsan lacus vel facilisis.</p>
  <div class="btn hero-cta">Contact Us</div>
  <div class="video">
    <div>V<br>I<br>D<br>E<br>O</div>
    <div class="play"><svg width="16" height="16" viewBox="0 0 16 16"><path d="M4 2l10 6-10 6z" fill="#fff"/></svg></div>
    <div>P<br>L<br>A<br>Y</div>
  </div>
</header>
<div class="mouse"><svg width="24" height="36" viewBox="0 0 24 36"><rect x="2" y="2" width="20" height="32" rx="10" fill="none" stroke="#8b5a1f" stroke-width="2.5"/><line x1="12" y1="9" x2="12" y2="15" stroke="#8b5a1f" stroke-width="2.5" stroke-linecap="round"/></svg></div>

<!-- Services -->
<h2 class="section-title" style="top:704px">Our Services</h2>
<svg class="arrow" style="left:76px;top:990px" viewBox="0 0 30 50"><path d="M24 4L6 25l18 21" fill="none" stroke="#8b5a1f" stroke-width="3"/></svg>
<svg class="arrow" style="left:1094px;top:990px" viewBox="0 0 30 50"><path d="M6 4l18 21L6 46" fill="none" stroke="#8b5a1f" stroke-width="3"/></svg>

<article class="svc" style="left:140px">
  <div class="ph" role="img" aria-label="Silhouettes of business people shaking hands in an office"></div>
  <div class="svc-icon"></div>
  <h3>Business Sales</h3>
  <p>We are specialist brokers working with you to position your business to ensure it has the best possible results when selling.</p>
  <span class="link" style="left:32px;top:388px">Find Out More</span>
</article>
<article class="svc" style="left:452px">
  <div class="ph" role="img" aria-label="Close-up of a handshake in bright light" style="background:linear-gradient(135deg,#eef2f7,#8a95a3)"></div>
  <div class="svc-icon"></div>
  <h3>Mergers and Acquisitions</h3>
  <p>If you're considering the sale of your larger business, Quarry Vale Trade Partners is here to amplify your potential. Our dedication to your</p>
  <span class="link" style="left:32px;top:388px">Find Out More</span>
</article>
<article class="svc" style="left:764px">
  <div class="ph" role="img" aria-label="Team of consultants reviewing charts around a table" style="background:linear-gradient(135deg,#d9d4cc,#5b6170)"></div>
  <div class="svc-icon"></div>
  <h3>Business Consulting</h3>
  <p>With our dedicated team of you business consultants you are have working with people who experience growing existing businesses as well</p>
  <span class="link" style="left:32px;top:388px">Find Out More</span>
</article>

<!-- Selling process -->
<section class="process"></section>
<h2 class="section-title" style="top:1392px">Selling Process</h2>
<svg class="abs" style="left:296px;top:1530px" width="610" height="80" viewBox="0 0 610 80">
  <path d="M0 40 Q93 -10 186 40 T422 40 T610 40" fill="none" stroke="#8b5a1f" stroke-width="1.5" stroke-dasharray="5 4"/>
</svg>
<div class="step" style="left:129px">
  <div class="step-circle"><svg width="40" height="56" viewBox="0 0 40 56"><text x="20" y="46" text-anchor="middle" font-family="Poppins,sans-serif" font-size="52" font-weight="600" fill="#fff">$</text></svg></div>
  <h4>Appraisal</h4>
  <p>We specialise in the marketing, listing and selling of your business.</p>
</div>
<div class="step" style="left:367px">
  <div class="step-circle"><svg width="48" height="54" viewBox="0 0 48 54" fill="none" stroke="#fff" stroke-width="2.5"><rect x="5" y="7" width="38" height="44" rx="3"/><rect x="16" y="3" width="16" height="8" rx="2"/><path d="M12 22l3 3 5-6M24 22h12M12 33l3 3 5-6M24 33h12M24 43h12"/></svg></div>
  <h4>Prepare</h4>
  <p>Gather all documentation and prepare the documentation needed during Due Diligence.</p>
</div>
<div class="step" style="left:603px">
  <div class="step-circle"><svg width="56" height="50" viewBox="0 0 56 50" fill="none" stroke="#fff" stroke-width="2.5"><circle cx="30" cy="16" r="9"/><path d="M4 36h10l10 6h18l10-8M14 36l8-6h12"/></svg></div>
  <h4>Offer</h4>
  <p>Expert negotiations to ensure you have the best results.</p>
</div>
<div class="step" style="left:839px">
  <div class="step-circle"><svg width="60" height="40" viewBox="0 0 60 40" fill="none" stroke="#fff" stroke-width="2.5"><path d="M2 8h12l10 6 8-4h12l14 6v14H46L32 36 18 26H2z"/><path d="M24 14l8 8"/></svg></div>
  <h4>Sold</h4>
  <p>Due Diligence and finalisation of the sales process.</p>
</div>
<div class="btn" style="left:537px;top:1810px;width:126px;height:45px">Get Started</div>

<!-- Featured -->
<section class="featured" role="img" aria-label="Faded backdrop of business premises"></section>
<h2 class="section-title" style="top:1985px">Featured Businesses</h2>
<svg class="arrow" style="left:76px;top:2220px" viewBox="0 0 30 50"><path d="M24 4L6 25l18 21" fill="none" stroke="#8b5a1f" stroke-width="3"/></svg>
<svg class="arrow" style="left:1094px;top:2220px" viewBox="0 0 30 50"><path d="M6 4l18 21L6 46" fill="none" stroke="#8b5a1f" stroke-width="3"/></svg>
<article class="feat" style="left:140px" role="img" aria-label="Domestic cleaning in a living room">
  <h3>UNDER OFFER - Domestic Services Provider Run Under Management</h3>
  <div class="price">$450,000</div>
  <div class="btn">Under Contract</div>
</article>
<article class="feat" style="left:614px;background:linear-gradient(160deg,#5e5a55,#232120)" role="img" aria-label="Camper trailer showroom floor">
  <h3>UNDER OFFER - Camper Trailer Superstore</h3>
  <div class="price">$399,000 <small>+ SAV</small></div>
  <div class="btn">Under Contract</div>
</article>

<!-- Quick links -->
<h2 class="section-title" style="top:2574px">Quick Links</h2>
<a class="ql" style="left:140px" role="img" aria-label="Hand writing with a pen beside a coffee cup"><span>Market Appraisal</span></a>
<a class="ql" style="left:374px;background:linear-gradient(180deg,#a99d8c,#3a342c)" role="img" aria-label="Colleagues celebrating with a high five"><span>Recently Sold</span></a>
<a class="ql" style="left:606px;background:linear-gradient(180deg,#dcdcdc,#4a4a4a)" role="img" aria-label="Tall office buildings from below"><span>Why Sell With Us</span></a>
<a class="ql" style="left:840px;background:linear-gradient(180deg,#e6e6e6,#2b2b2b)" role="img" aria-label="Laptop on a desk"><span>News</span></a>

<!-- Recently sold -->
<h2 class="section-title" style="top:2962px">Recently Sold</h2>
<p class="abs" style="left:0;top:3025px;width:1200px;text-align:center;font-size:14px;color:#333">Browse from a list of recently sold businesses.</p>
<article class="sold" style="left:140px">
  <div class="ph" role="img" aria-label="Coffee shop counter with a display cabinet"></div>
  <span class="cfp">Contact for price</span><span class="tag">Sold</span>
  <h4>SOLD - Cosy Corner Coffee Shop</h4>
  <div class="loc"><svg width="14" height="18" viewBox="0 0 14 18"><path d="M7 0a7 7 0 0 0-7 7c0 5 7 11 7 11s7-6 7-11a7 7 0 0 0-7-7z" fill="#222"/><circle cx="7" cy="7" r="2.5" fill="#fff"/></svg>Macquarie ACT</div>
</article>
<article class="sold" style="left:452px">
  <div class="ph" role="img" aria-label="Burger and fries on a tray" style="background:linear-gradient(180deg,#8c7158,#2c241d)"></div>
  <span class="cfp">Contact for price</span><span class="tag">Sold</span>
  <h4>SOLD - Popular Burger Joint in Adel</h4>
  <div class="loc"><svg width="14" height="18" viewBox="0 0 14 18"><path d="M7 0a7 7 0 0 0-7 7c0 5 7 11 7 11s7-6 7-11a7 7 0 0 0-7-7z" fill="#222"/><circle cx="7" cy="7" r="2.5" fill="#fff"/></svg>Prospect SA</div>
</article>
<article class="sold" style="left:764px">
  <div class="ph" role="img" aria-label="Diners seated in a busy bar and cafe" style="background:linear-gradient(180deg,#9a9184,#342f2a)"></div>
  <span class="cfp">Contact for price</span><span class="tag">Sold</span>
  <h4>SOLD - Bar and Cafe overlooking</h4>
  <div class="loc"><svg width="14" height="18" viewBox="0 0 14 18"><path d="M7 0a7 7 0 0 0-7 7c0 5 7 11 7 11s7-6 7-11a7 7 0 0 0-7-7z" fill="#222"/><circle cx="7" cy="7" r="2.5" fill="#fff"/></svg>Ulladulla NSW</div>
</article>
<div class="btn" style="left:490px;top:3478px;width:220px;height:44px">View More Sold Businesses</div>

<!-- Team -->
<section class="team">
  <h2 class="section-title" style="top:76px;color:#fff">Meet Our Team</h2>
  <p class="abs" style="left:0;top:140px;width:1200px;text-align:center;font-size:14px;color:#eee">Get to know our professional, enthusiastic, and dedicated team.</p>
  <div class="member" style="left:185px">
    <div class="ph" role="img" aria-label="Portrait of the managing director outdoors"></div>
    <h3>Darren Holloway</h3>
    <p>Managing Director | Business Broker | Business Consultant<br>- (02) 5384 9027</p>
  </div>
  <div class="member" style="left:628px">
    <div class="ph" role="img" aria-label="Portrait of the managing partner outdoors" style="background:linear-gradient(135deg,#777,#cfcfcf)"></div>
    <h3>Tessa Holloway</h3>
    <p>Managing Partner | Business Consultant<br>- (02) 5384 9027</p>
  </div>
</section>

<!-- News -->
<h2 class="section-title" style="top:4357px">Latest News &amp; Tips</h2>
<svg class="arrow" style="left:76px;top:4598px" viewBox="0 0 30 50"><path d="M24 4L6 25l18 21" fill="none" stroke="#8b5a1f" stroke-width="3"/></svg>
<svg class="arrow" style="left:1094px;top:4598px" viewBox="0 0 30 50"><path d="M6 4l18 21L6 46" fill="none" stroke="#8b5a1f" stroke-width="3"/></svg>
<article class="news" style="left:148px">
  <svg class="ph" viewBox="0 0 293 180" role="img" aria-label="Bar chart of annual change by industry">
    <rect width="293" height="180" fill="#fff"/>
    <g fill="#3b5ba5">
      <rect x="150" y="20" width="60" height="5"/><rect x="150" y="30" width="48" height="5"/><rect x="150" y="40" width="40" height="5"/><rect x="150" y="50" width="70" height="5"/><rect x="150" y="60" width="34" height="5"/><rect x="150" y="70" width="28" height="5"/><rect x="150" y="80" width="52" height="5"/><rect x="150" y="90" width="22" height="5"/><rect x="150" y="100" width="18" height="5"/><rect x="150" y="110" width="44" height="5"/><rect x="150" y="120" width="12" height="5"/><rect x="150" y="130" width="26" height="5"/><rect x="150" y="140" width="8" height="5"/>
    </g>
    <g fill="#bbb"><rect x="40" y="20" width="100" height="3"/><rect x="50" y="30" width="90" height="3"/><rect x="60" y="40" width="80" height="3"/><rect x="45" y="50" width="95" height="3"/><rect x="55" y="60" width="85" height="3"/><rect x="40" y="70" width="100" height="3"/><rect x="60" y="80" width="80" height="3"/><rect x="50" y="90" width="90" height="3"/><rect x="45" y="100" width="95" height="3"/><rect x="55" y="110" width="85" height="3"/><rect x="40" y="120" width="100" height="3"/><rect x="60" y="130" width="80" height="3"/><rect x="50" y="140" width="90" height="3"/></g>
    <line x1="150" y1="15" x2="150" y2="150" stroke="#999"/>
    <line x1="150" y1="150" x2="280" y2="150" stroke="#999"/>
  </svg>
  <div class="date"><svg width="14" height="14" viewBox="0 0 14 14" fill="none" stroke="#333"><rect x="1" y="2" width="12" height="11"/><path d="M1 5h12M4 0v3M10 0v3"/></svg>November 12, 2023</div>
  <h4>Trending Industries</h4>
  <p>The latest data released from the National Statistics Office (NSO) shows strong growth across most services style</p>
  <span class="link">Read More</span>
</article>
<article class="news" style="left:452px">
  <div class="ph" role="img" aria-label="Woman at a laptop shrugging with uncertainty" style="background:linear-gradient(135deg,#e8e8e8,#555)"></div>
  <div class="date"><svg width="14" height="14" viewBox="0 0 14 14" fill="none" stroke="#333"><rect x="1" y="2" width="12" height="11"/><path d="M1 5h12M4 0v3M10 0v3"/></svg>November 12, 2023</div>
  <h4>Buying a Business for Beginners:</h4>
  <p>Are you considering taking the leap into business ownership by purchasing an existing enterprise? Buying a business can</p>
  <span class="link">Read More</span>
</article>
<article class="news" style="left:755px">
  <div class="ph" role="img" aria-label="Illustration of a money bag with coins on a teal background" style="background:linear-gradient(135deg,#5fb6b0,#2f8a86)"></div>
  <div class="date"><svg width="14" height="14" viewBox="0 0 14 14" fill="none" stroke="#333"><rect x="1" y="2" width="12" height="11"/><path d="M1 5h12M4 0v3M10 0v3"/></svg>November 12, 2023</div>
  <h4>Exploring Vendor Finance: Pros and</h4>
  <p>Selling a business is a significant decision, one that often comes with various financial considerations. While most business</p>
  <span class="link">Read More</span>
</article>

<!-- Footer -->
<footer class="footer">
  <div class="fcol" style="left:142px">
    <h5>QUICK LINKS</h5>
    <ul><li>Browse All Businesses</li><li>Request Appraisal</li><li>About Us</li><li>Contact</li></ul>
  </div>
  <div class="fcol" style="left:355px">
    <h5>CONTACT DETAILS</h5>
    <div class="contact-row"><svg width="12" height="16" viewBox="0 0 14 18"><path d="M7 0a7 7 0 0 0-7 7c0 5 7 11 7 11s7-6 7-11a7 7 0 0 0-7-7z" fill="#ddd"/><circle cx="7" cy="7" r="2.5" fill="#1b1b1b"/></svg>Australia Wide</div>
    <div class="contact-row"><svg width="12" height="14" viewBox="0 0 14 14"><path d="M3 1l3 3-2 2c1 2 2 3 4 4l2-2 3 3-2 2C6 13 1 8 1 3z" fill="#ddd"/></svg><span>Phone<br>(02) 5384 9027</span></div>
    <div class="contact-row"><svg width="14" height="12" viewBox="0 0 14 12"><rect x="1" y="1" width="12" height="10" fill="none" stroke="#ddd"/><path d="M1 1l6 5 6-5" fill="none" stroke="#ddd"/></svg><span>Email<br>hello@qvtrades.com.au</span></div>
  </div>
  <div class="fcol" style="left:663px">
    <h5>FOLLOW US</h5>
    <div class="social-row"><span class="social-dot"></span>Community</div>
    <div class="social-row"><span class="social-dot"></span>Updates</div>
    <div class="social-row"><span class="social-dot"></span>Network</div>
    <div class="social-row"><span class="social-dot"></span>Gallery</div>
  </div>
  <div class="foot-brand"><div class="brand-dot"></div>Quarry Vale Trade Partners</div>
</footer>
<div class="bottom-bar">© 2023 - 2024 | Quarry Vale Trade Partners , All Rights Reserved | Privacy Policy. Powered by Harbour Pixel Studio</div>

</body>
</html>
```